Business Card Design for Varnel

I've already got the logo, but I'd like to see some interesting designs.

I don't want anything to complex. I like it simple,yet innovative, like the logo.

My business is System Administration for small to medium size businesses, so that will be my main target audience.
Updates

hey all, the png has been uploaded.

Hey all,

If you are submitting the back side of the card, I'd like the top bit of the card to be Varnel Solutions and the logo, the bottom of the card the website, with a white background.

The middle I'd like to leave blank for a quote that will be printed on each card.

Thanks!

Doug

Industry/Entity Type

Business

```html
<!DOCTYPE html>
<html lang="en">
<head>
<meta charset="utf-8">
<title>Varnel Solutions – Business Card</title>
<link rel="stylesheet" href="https://fonts.googleapis.com/css2?family=Open+Sans:wght@400;500;600&display=swap">
<style>
  :root {
    --card-bg: #eef1f2;
    --card-glow: #ffffff;
    --brand-blue: #2a83e4;
    --brand-blue-soft: #3d8fe6;
    --faint-mark: #cfe2ee;
    --ink: #141414;
    --icon-ink: #161616;
    --icon-line: #ffffff;
  }
  * { margin: 0; padding: 0; box-sizing: border-box; }
  html, body {
    width: 1200px; height: 720px; overflow: hidden;
    background: var(--card-bg);
  }
  .card {
    position: relative;
    width: 1200px; height: 720px; overflow: hidden;
    background: radial-gradient(ellipse 520px 420px at 1000px 260px, var(--card-glow) 0%, var(--card-bg) 100%);
    font-family: "Open Sans", Arial, sans-serif;
    color: var(--ink);
  }
  .backdrop { position: absolute; inset: 0; width: 1200px; height: 720px; }
  .brand {
    position: absolute; left: 78px; top: 72px;
    display: flex; align-items: center; gap: 18px;
  }
  .brand-dot {
    width: 58px; height: 58px; border-radius: 50%;
    background: var(--brand-blue-soft);
  }
  .brand-name {
    font-size: 44px; font-weight: 600; letter-spacing: -0.5px;
    color: var(--brand-blue-soft); line-height: 1;
  }
  .identity {
    position: absolute; left: 0; right: 0; top: 186px;
    text-align: center; transform: translateX(17px);
  }
  .person-name {
    font-size: 98px; font-weight: 400; line-height: 1; letter-spacing: 1px;
  }
  .person-role {
    margin-top: 16px;
    font-size: 31px; font-weight: 400; letter-spacing: 6px; line-height: 1;
  }
  .contact-row {
    position: absolute; display: flex; align-items: center;
    line-height: 1; white-space: nowrap;
  }
  .contact-row.address { left: 133px; top: 537px; font-size: 38px; gap: 26px; }
  .contact-row.lines { left: 87px; top: 598px; font-size: 30px; }
  .contact-item { display: flex; align-items: center; gap: 8px; }
  .contact-item + .contact-item { margin-left: 8px; }
  .contact-item.web { margin-left: 24px; }
  .icon { flex: none; width: 43px; height: 43px; }
  .address .icon { width: 44px; height: 44px; }
</style>
</head>
<body>
<main class="card">
  <svg class="backdrop" viewBox="0 0 1200 720" aria-hidden="true">
    <circle class="faint-mark" cx="617" cy="300" r="200" fill="var(--faint-mark)" opacity="0.55"/>
    <path class="wave" fill="var(--brand-blue)"
      d="M0,720 L0,645 C120,575 280,478 368,456 C352,530 345,620 352,700 C470,635 720,592 1200,584 L1200,720 Z"/>
  </svg>

  <header class="brand">
    <span class="brand-dot"></span>
    <span class="brand-name">Varnel Solutions</span>
  </header>

  <section class="identity">
    <h1 class="person-name">NAME</h1>
    <p class="person-role">MARKETING DIRECTOR</p>
  </section>

  <p class="contact-row address">
    <svg class="icon" viewBox="0 0 44 44" aria-hidden="true">
      <circle cx="22" cy="22" r="22" fill="var(--icon-ink)"/>
      <path d="M14 23 L22 15 L30 23 M17 21 V29 H27 V21 M20 29 V24 H24 V29" fill="none" stroke="var(--icon-line)" stroke-width="2" stroke-linejoin="round"/>
    </svg>
    <span>418 ALDER ROW, FAIRMONT, CA 93410</span>
  </p>

  <p class="contact-row lines">
    <span class="contact-item phone">
      <svg class="icon" viewBox="0 0 44 44" aria-hidden="true">
        <circle cx="22" cy="22" r="22" fill="var(--icon-ink)"/>
        <path d="M22 14 C16.5 14 13 17.5 13 21.5 C13 25.5 16.5 28.5 21 28.5 L17 31 C22 31 25 29.5 27 27.5 C29.5 26 31 24 31 21.5 C31 17.5 27.5 14 22 14 Z" fill="none" stroke="var(--icon-line)" stroke-width="2" stroke-linejoin="round"/>
      </svg>
      <span>P: 555 014 273</span>
    </span>
    <span class="contact-item email">
      <svg class="icon" viewBox="0 0 44 44" aria-hidden="true">
        <circle cx="22" cy="22" r="22" fill="var(--icon-ink)"/>
        <path d="M14 19 V30 H30 V19 M14 19 L22 25 L30 19 M17 19 V13 H27 V19" fill="none" stroke="var(--icon-line)" stroke-width="2" stroke-linejoin="round"/>
      </svg>
      <span>HELLO@VARNELMAIL.COM</span>
    </span>
    <span class="contact-item web">WWW.VARNELSYS.COM</span>
  </p>
</main>
</body>
</html>
```